EPIC, awesome, creative business card needed - get involved!

I'm launching a boutique, exclusive Property Management real estate agency in Sydney early next year.
The name of the agency will be called "Quartz Hill Lane" - it's a play on "chase the silver pebble trail" to wealth. The Quartz Hill Lane signifies wealth through property investment.
My business will offer management of investment properties (ie Property Management).
The difference with Quartz Hill Lane and other agencies is the business will be run by one of Australia's leading property investment experts, and also one of Australia's leading property managers.
It will be exclusively for high net worth properties and individuals, so the business card needs to be extremely sharp, slick and relatively simple.
The information I want on the card is as follows
Nolan Pryce - Director
M: 0412 967 154
P: 9735 6021
E: nolan@quartzhilllane.net.au
W: quartzhilllane.net.au
I'm happy with the red from the logo, black - no yellows or funky colors. I want this to be a super corporate and slick business card to match the high end nature of the business.
Good luck everyone, and please ask questions for clarification.

```html
<!DOCTYPE html>
<html lang="en">
<head>
<meta charset="utf-8">
<title>Quartz Hill Lane – Business Card</title>
<link rel="stylesheet" href="https://fonts.googleapis.com/css2?family=Oswald:wght@300;400&display=swap">
<style>
  :root {
    --stage: #2b2725;
    --card-red: #c8080d;
    --panel-red: #a80509;
    --ink-white: #ffffff;
    --ink-soft: #f6dcdc;
    --edge-black: #0d0b0b;
  }
  * { margin: 0; padding: 0; box-sizing: border-box; }
  html, body {
    width: 1200px;
    height: 716px;
    overflow: hidden;
    background: var(--stage);
  }
  .canvas {
    position: relative;
    width: 1200px;
    height: 716px;
    font-family: "Oswald", sans-serif;
  }
  .card {
    position: absolute;
    background: var(--card-red);
    border-bottom: 4px solid var(--edge-black);
    box-shadow: 0 18px 40px rgba(0, 0, 0, 0.45);
  }

  /* Front face */
  .card--front {
    left: 90px;
    top: 208px;
    width: 520px;
    height: 300px;
  }
  .name-panel {
    position: absolute;
    left: 50%;
    top: 50%;
    width: 190px;
    height: 190px;
    transform: translate(-50%, -50%);
    background: var(--panel-red);
    display: flex;
    align-items: center;
    justify-content: center;
  }
  .name-panel__text {
    color: var(--ink-white);
    font-weight: 400;
    font-size: 36px;
    line-height: 1.02;
    letter-spacing: 1px;
    text-transform: uppercase;
  }

  /* Back face */
  .card--back {
    left: 720px;
    top: 108px;
    width: 300px;
    height: 500px;
  }
  .contact {
    position: absolute;
    left: 34px;
    bottom: 40px;
    color: var(--ink-white);
  }
  .contact__name {
    font-weight: 400;
    font-size: 22px;
    letter-spacing: 2px;
    text-transform: uppercase;
    line-height: 1.1;
  }
  .contact__role {
    font-weight: 300;
    font-size: 13px;
    letter-spacing: 1px;
    color: var(--ink-soft);
    margin-bottom: 44px;
  }
  .contact__list {
    list-style: none;
    font-weight: 300;
    font-size: 15px;
    letter-spacing: 0.8px;
    line-height: 1.6;
  }
  .contact__label {
    display: inline-block;
    width: 18px;
    font-weight: 400;
  }
</style>
</head>
<body>
  <main class="canvas">
    <section class="card card--front" aria-label="Card front">
      <div class="name-panel">
        <span class="name-panel__text">Quartz<br>Hill<br>Lane</span>
      </div>
    </section>

    <section class="card card--back" aria-label="Card back">
      <div class="contact">
        <p class="contact__name">Nolan Pryce</p>
        <p class="contact__role">Director</p>
        <ul class="contact__list">
          <li><span class="contact__label">M</span>0412 967 154</li>
          <li><span class="contact__label">T</span>9735 6021</li>
          <li>nolan@quartzhilllane.net.au</li>
          <li>quartzhilllane.net.au</li>
        </ul>
      </div>
    </section>
  </main>
</body>
</html>
```